Website re-design for a Gardening - Vegetable Growing -Compost Ecommerce site

We need a "green & organic" looking web design for The Loam Barrow website re-design. The website sells garden and landscape supplies, and specialises in composites and vegetable growing products which are sold nationwide throughout the UK.

This project is for a homepage & content page design which can be used as a template to create other pages through the site, ideally with css and coding for a joomla template.

Our customer base is made up of gardeners & vegetable growers. The site is an ecommerce site run on Joomla CMS, we will be converting the design into a joomla template.

The Home page will contain information and attractive garden & vegetable growing images linking to information and product / shop category pages.

Current site: www.theloambarrow.co.uk

Sites I like the look of :

http://fernquillplot.com/index.php
http://albumpage.stationnine.com
http://www.squirmydelvers.co.uk/
http://www.hamletcreamery.co.uk
Updates

Hi Guys! Feel free to use different colour schemes from the three colours i have suggested in the brief. I am open to any suggestions, but a modern look and feel is preferred.

Target Market(s)

Home owners, vegetable growers and keen gardeners

Industry/Entity Type

Landscape

Coding

Coded - Design and coding required

Font styles to use
Sans Serif

Colors
9bcb3c
faa54b
fece3e

Requirements
Must have
• a white main content background

```html
<!DOCTYPE html>
<html lang="en">
<head>
<meta charset="utf-8">
<title>The Loam Barrow – Home</title>
<link href="https://fonts.googleapis.com/css2?family=Open+Sans:wght@400;600;700&family=Archivo+Black&display=swap" rel="stylesheet">
<style>
:root{
  --green:#9bcb3c;
  --orange:#faa54b;
  --orange-deep:#f7983a;
  --dark:#2d2d2d;
  --text:#444;
  --muted:#9a9a9a;
  --white:#fff;
}
*{margin:0;padding:0;box-sizing:border-box}
html,body{width:737px;height:1200px;overflow:hidden;background:var(--white)}
body{position:relative;font-family:"Open Sans",Arial,sans-serif;color:var(--text)}
.abs{position:absolute}
/* header */
.logo{left:100px;top:20px;display:flex;align-items:center;gap:7px}
.logo-dot{width:26px;height:26px;border-radius:50%;background:var(--orange)}
.logo-name{font-size:19px;font-weight:600;color:var(--green);letter-spacing:.2px}
.cart-total{left:539px;top:17px;font-size:7.5px;color:var(--orange)}
.cart-btn{left:599px;top:11px;width:38px;height:21px;background:#4a4a4a;display:flex;align-items:center;justify-content:center}
.search{left:470px;top:46px;width:169px;height:24px;border:1px solid #cfcfcf;border-radius:2px;font-size:6.5px;color:#999;padding:8px 0 0 6px}
.search svg{position:absolute;right:5px;top:5px}
/* nav */
.nav{left:0;top:82px;width:737px;height:32px;background:var(--green)}
.nav a{position:absolute;top:0;height:32px;line-height:32px;color:var(--white);font-size:7.3px;text-decoration:none;letter-spacing:.2px}
.nav a.active{background:var(--orange);text-align:center}
.nav-shadow{left:0;top:114px;width:737px;height:8px;background:linear-gradient(#d9d9d9,#fff)}
/* hero */
.hero{left:0;top:122px;width:737px;height:358px;background:radial-gradient(ellipse at 62% 35%,#9fc83b 0,#5d7a23 18%,#2e2c12 45%,#1f1a0f 75%),#231c10}
.hero-soil{left:0;top:390px;width:737px;height:90px;background:linear-gradient(rgba(40,30,18,0),#3a2c1c 60%,#2a2015)}
.caption{left:100px;top:322px;width:432px;height:97px}
.caption h1{position:absolute;left:17px;top:13px;font-size:13px;font-weight:700;color:var(--white);letter-spacing:.6px}
.caption p{position:absolute;left:17px;top:36px;font-size:9.6px;color:#eaeaea}
.shop-btn{left:20px;top:62px;width:91px;height:25px;background:var(--orange);border:1px solid #fff;color:#5a3410;font-size:9px;text-align:center;line-height:23px}
.dot{top:449px;width:9px;height:9px;border-radius:50%;background:var(--white)}
/* banner */
.banner{left:139px;top:494px;width:456px;height:53px;background:var(--orange)}
.banner .big{position:absolute;left:14px;top:6px;font-family:"Archivo Black",Arial,sans-serif;color:var(--white);font-size:15.5px;line-height:22px;text-align:center;letter-spacing:.5px}
.banner .call{position:absolute;left:157px;top:16px;font-size:13px;color:#fff3e4}
.banner .call b{font-weight:400;color:var(--white)}
/* intro */
.intro{left:104px;top:567px;width:262px;font-size:6.4px;line-height:11.5px;color:var(--muted)}
.intro p+p{margin-top:12px}
.box{background:var(--orange);color:var(--white);font-size:6.5px;padding:8px 6px}
.box li{list-style:none;line-height:13.3px;padding-left:20px;position:relative}
.box li::before{content:"";position:absolute;left:6px;top:4px;width:5px;height:2.5px;border-left:1.3px solid #fff;border-bottom:1.3px solid #fff;transform:rotate(-45deg)}
.sellers{left:378px;top:569px;width:117px;height:93px}
.order{left:512px;top:569px;width:117px;height:93px;padding-top:11px}
.order .lead{line-height:13.3px;margin-bottom:0}
.top-badge{left:609px;top:553px;width:30px;height:30px;border-radius:50%;background:var(--orange);border:1px solid #fff;box-shadow:0 0 0 1px var(--orange);color:var(--white);font-size:7px;text-align:center;line-height:28px}
/* products */
.products-title{left:0;top:686px;width:737px;text-align:center;font-size:15px;color:#555}
.arrow{top:686px;width:15px;height:15px;background:#c9c9c9;display:flex;align-items:center;justify-content:center}
.photo{top:715px;width:168px;height:83px}
.p-title{top:807px;font-size:8px;color:#444}
.p-text{top:824px;width:168px;font-size:6.4px;line-height:11px;color:var(--muted)}
.p-text p+p{margin-top:5px}
.buy{top:888px;height:22px;background:var(--orange);color:#4a2a08;font-size:6.8px;line-height:22px;text-align:center;box-shadow:0 1px 2px rgba(0,0,0,.2)}
.add{top:890px;width:39px;height:20px;background:var(--green);color:var(--white);font-size:6.6px;line-height:20px;text-align:center}
.cart-icon{top:891px}
/* footer */
.footer{left:0;top:932px;width:737px;height:192px;background:var(--dark);color:#ddd}
.f-col{top:14px;font-size:6.2px;line-height:11.6px}
.f-col h3{font-size:8.6px;font-weight:400;color:var(--white);margin-bottom:8px}
.f-col p+p{margin-top:6px}
.f-col li{list-style:none;padding-left:12px;position:relative;line-height:15.3px}
.f-col li::before{content:"";position:absolute;left:0;top:6px;width:4px;height:4px;border-radius:50%;background:#aaa}
.social{top:153px;width:15px;height:15px;border-radius:2px}
.news-label{left:264px;top:160px;font-size:7.5px;color:var(--white)}
.news-sep{left:328px;top:148px;width:1px;height:30px;background:#555}
.news-text{left:339px;top:150px;width:135px;font-size:5.4px;line-height:10.8px;color:#ccc}
.news-input{left:488px;top:151px;width:140px;height:22px;background:#f2f2f2;font-size:5.4px;color:#888;padding:7px 0 0 26px}
.bottom{left:0;top:1124px;width:737px;height:76px;background:var(--orange);color:#3a2206;text-align:center;font-size:5.8px;line-height:9.3px}
.bottom .copy{color:var(--white);font-size:6.4px;margin:11px 0 6px}
.code{right:35px;top:1163px;font-size:5.8px;color:#3a2206}
</style>
</head>
<body>

<header>
  <div class="abs logo"><span class="logo-dot"></span><span class="logo-name">The Loam Barrow</span></div>
  <div class="abs cart-total">Cart - £0.00</div>
  <div class="abs cart-btn">
    <svg width="24" height="12" viewBox="0 0 24 12" fill="none" stroke="#fff" stroke-width="1.3"><path d="M1 1h3l2 7h8l2-5H5"/><circle cx="7" cy="10.5" r="1"/><circle cx="13" cy="10.5" r="1"/><path d="M19 4l2 2 2-2"/></svg>
  </div>
  <div class="abs search">Search...
    <svg width="13" height="13" viewBox="0 0 13 13" fill="none" stroke="#999" stroke-width="1.4"><circle cx="5.5" cy="5.5" r="4.3"/><path d="M8.6 8.6l3.4 3.4"/></svg>
  </div>
</header>

<nav class="abs nav">
  <a class="active" href="#" style="left:99px;width:71px">HOME</a>
  <a href="#" style="left:190px">PRODUCTS</a>
  <a href="#" style="left:274px">ABOUT US</a>
  <a href="#" style="left:355px">GARDEN GURU</a>
  <a href="#" style="left:453px">BULK LOADS</a>
  <a href="#" style="left:544px">GOTO CHECK OUT</a>
</nav>
<div class="abs nav-shadow"></div>

<section>
  <div class="abs hero" role="img" aria-label="Close-up of a young green seedling sprouting from dark soil"></div>
  <div class="abs hero-soil"></div>
  <div class="abs caption">
    <svg class="abs" width="432" height="97" style="left:0;top:0"><path d="M0 0H375L432 97H0Z" fill="rgba(120,140,40,.45)"/></svg>
    <h1>COMPOST SUPPLIERS</h1>
    <p>Quality Compost, Manure, Topsoil and Grow Your Own Kit at Great Prices</p>
    <div class="abs shop-btn">Shop Here</div>
  </div>
  <span class="abs dot" style="left:350px;background:var(--orange);border:1px solid #fff"></span>
  <span class="abs dot" style="left:366px"></span>
  <span class="abs dot" style="left:382px"></span>
</section>

<div class="abs banner">
  <div class="big">SHOP ONLINE<br>click here</div>
  <div class="call">or call <b>0870 555 0142</b> to place an order.</div>
</div>

<section>
  <div class="abs intro">
    <p>We've got all the compost, topsoil and garden supplies you'll need to get your garden in shape this year! Whether you just need some compost to top up your flower beds or want to start growing your own fruit and veg, we have everything you'll need and much more!</p>
    <p>As the UK's leading supplier, we have an extensive range of growing media as well as many other garden products such as organic compost, vegetable growing kits and baby vegetable seedlings!</p>
  </div>
  <div class="abs box sellers">
    <div style="margin-bottom:3px">5 Best Sellers</div>
    <ul>
      <li>Organic Compost Bulk Bag</li>
      <li>Children's Veg Garden</li>
      <li>Mushroom Compost</li>
      <li>Vegetable Blend Topsoil</li>
      <li>Border Blend Topsoil</li>
    </ul>
  </div>
  <div class="abs box order">
    <div class="lead">Order online before 1.00pm<br>for next day</div>
    <ul>
      <li>Great Value</li>
      <li>Quality Service</li>
      <li>Fast Delivery</li>
      <li>The Finest Products</li>
    </ul>
  </div>
  <div class="abs top-badge">TOP</div>
</section>

<section>
  <h2 class="abs products-title" style="font-weight:400">Our Products</h2>
  <div class="abs arrow" style="left:606px"><svg width="6" height="8"><path d="M5 0L1 4l4 4" fill="none" stroke="#fff"/></svg></div>
  <div class="abs arrow" style="left:624px"><svg width="6" height="8"><path d="M1 0l4 4-4 4" fill="none" stroke="#fff"/></svg></div>

  <div class="abs photo" style="left:101px;background:radial-gradient(ellipse at 50% 55%,#3a2618 0,#2a1c12 45%,#e8c8b0 75%,#f3f3f3)" role="img" aria-label="Cupped hands holding dark compost"></div>
  <div class="abs photo" style="left:285px;background:linear-gradient(#4a86c8,#a9cbe8 55%,#e9c2a6 75%,#c9a084)" role="img" aria-label="Hands holding a green seedling in soil against a blue sky"></div>
  <div class="abs photo" style="left:470px;background:linear-gradient(#d8dde0,#c9cfcf 35%,#4d6a2e 55%,#5b4a36 80%,#6b5a44)" role="img" aria-label="Green screening machine on a yard of shredded manure"></div>

  <div class="abs p-title" style="left:101px">Bulk Loads of Topsoil &amp; Bark</div>
  <div class="abs p-title" style="left:285px">Buy Compost Online</div>
  <div class="abs p-title" style="left:470px">Manure Suppliers</div>

  <div class="abs p-text" style="left:101px"><p>As well as bulk loads of compost we supply bulk loads of topsoil, bark and woodchip in various grades.</p><p>Bulk loads can be delivered throughout the UK from part loads to 30 tonne articulated loads supplied.</p></div>
  <div class="abs p-text" style="left:285px"><p>Buy compost and manure online in bags or 1m3 bulk bags online as well as many other garden supplies. We also supply compost, topsoil and bark in bulk loads throughout the country.</p></div>
  <div class="abs p-text" style="left:470px"><p>We supply, well-rotted, shredded horse manure which is collected from racing stables where the horses enjoy a grass free diet.</p></div>

  <div class="abs buy" style="left:99px;width:68px">BULK LOADS</div>
  <svg class="abs cart-icon" style="left:195px" width="20" height="18" viewBox="0 0 20 18" fill="none" stroke="#333" stroke-width="1.4"><path d="M1 2h3l3 10h9l3-8H5"/><path d="M8 6h9M9 9h7"/><circle cx="8" cy="15.5" r="1.4"/><circle cx="15" cy="15.5" r="1.4"/></svg>
  <div class="abs add" style="left:230px">ADD CART</div>

  <div class="abs buy" style="left:283px;width:71px">BUY COMPOST</div>
  <svg class="abs cart-icon" style="left:382px" width="20" height="18" viewBox="0 0 20 18" fill="none" stroke="#333" stroke-width="1.4"><path d="M1 2h3l3 10h9l3-8H5"/><path d="M8 6h9M9 9h7"/><circle cx="8" cy="15.5" r="1.4"/><circle cx="15" cy="15.5" r="1.4"/></svg>
  <div class="abs add" style="left:414px">ADD CART</div>

  <div class="abs buy" style="left:468px;width:91px">BUY HORSE MANURE</div>
  <svg class="abs cart-icon" style="left:571px" width="20" height="18" viewBox="0 0 20 18" fill="none" stroke="#333" stroke-width="1.4"><path d="M1 2h3l3 10h9l3-8H5"/><path d="M8 6h9M9 9h7"/><circle cx="8" cy="15.5" r="1.4"/><circle cx="15" cy="15.5" r="1.4"/></svg>
  <div class="abs add" style="left:600px">ADD CART</div>
</section>

<footer class="abs footer">
  <div class="abs f-col" style="left:114px;width:136px">
    <h3>About Us</h3>
    <p>Lorem ipsum dolor sit amet, consectetur adipi scing elit. Vestibulum iaculis massa nec velit commodo lobortis.Quisque diam lacus, tinci-dunt vitae eros porta, sagittis rhoncus est. Quisque sed justo commodo lobortis.Quisque diam lacus, tincidunt vitae eros porta, sagittis rhoncus est. Quisque sed justo...........</p>
  </div>
  <div class="abs f-col" style="left:279px;width:112px">
    <h3>Delivery Info</h3>
    <p>Feel free to contact us if you have any problems.</p>
    <p>We deliver nationwide in bags and bulk bags and can deliver bulk loads to most areas. Most deliveries can be done next day!</p>
  </div>
  <div class="abs f-col" style="left:434px;width:110px;line-height:10.6px">
    <h3>Customer Services</h3>
    <p>Sales Office 12 Mill Lane,<br>Ashcombe Wessexshire<br>AB1 2CD</p>
    <p>tel : 0870 555 0142<br>Fax : 01632 960 418<br>Email.<br>info@theloambarrow.co.uk</p>
  </div>
  <div class="abs f-col" style="left:564px">
    <h3>Why Choose Us</h3>
    <ul>
      <li>Shipping &amp; Returns</li>
      <li>Secure Shopping</li>
      <li>International Shipping</li>
      <li>Affiliates</li>
      <li>Group Sales</li>
    </ul>
  </div>
  <span class="abs social" style="left:123px;background:#3b5ca0"></span>
  <span class="abs social" style="left:144px;background:#3aa2e0"></span>
  <span class="abs social" style="left:165px;background:#f39a1e"></span>
  <span class="abs social" style="left:186px;background:#d8322e"></span>
  <span class="abs social" style="left:207px;background:#5ab9c9"></span>
  <div class="abs news-label">NEWSLETTER :</div>
  <div class="abs news-sep"></div>
  <div class="abs news-text">In venenatis neque a eros laoreet eu placerat erat suscipit. Fusce cursus, erat ut scelerisque condimentum</div>
  <div class="abs news-input">Enter Your Email Address :
    <svg class="abs" style="left:5px;top:7px" width="13" height="9" viewBox="0 0 13 9"><rect width="13" height="9" fill="var(--green)"/><path d="M0 0l6.5 5L13 0" fill="none" stroke="#fff"/></svg>
    <svg class="abs" style="right:7px;top:7px" width="5" height="8"><path d="M1 0l3 4-3 4" fill="none" stroke="#999"/></svg>
  </div>
</footer>

<div class="abs bottom">
  <div class="copy">© 2013 The Loam Barrow</div>
  <div>The Loam Barrow is owned &amp; operated by Fieldstead Garden Supplies Ltd | Co. Registration Number: 1234567 | VAT Reg. No: 123 4567 89</div>
  <div>Fieldstead Garden Supplies Ltd, 12 Mill Lane, Ashcombe Wessexshire, AB1 2CD</div>
  <div>Tel. 0870 555 0142 (calls cost from 10p per minute)</div>
  <div>Terms &amp; Conditions &nbsp;- Delivery - Site Map - links</div>
</div>
<div class="abs code">D4</div>

</body>
</html>
```